KORBALT

The business want a professional looking business card. We have a scetch we will add but want the extra upgrade, and would like more suggestions for variations of our business cards.

```html
<!DOCTYPE html>
<html lang="en">
<head>
<meta charset="utf-8">
<title>KORBALT – Business Card</title>
<link rel="stylesheet" href="https://fonts.googleapis.com/css2?family=Lexend+Deca:wght@300&family=Playfair+Display:wght@400&display=swap">
<style>
  :root {
    --navy: #0757a0;
    --sky: #3780c0;
    --white: #ffffff;
    --sans: "Lexend Deca", sans-serif;
    --serif: "Playfair Display", serif;
  }
  * { margin: 0; padding: 0; box-sizing: border-box; }
  html, body { width: 1050px; height: 1200px; overflow: hidden; background: var(--sky); }
  .canvas { position: relative; width: 1050px; height: 1200px; background: var(--sky); color: var(--white); }

  .card-front { position: absolute; left: 0; top: 0; width: 1050px; height: 600px; overflow: hidden; }
  .card-front__shapes { position: absolute; inset: 0; }

  .identity { position: absolute; left: 60px; width: 450px; top: 193px; text-align: center; }
  .identity__name { font-family: var(--sans); font-weight: 300; font-size: 30px; letter-spacing: 0.5px; line-height: 1.1; }
  .identity__role { font-family: var(--sans); font-weight: 300; font-size: 18px; letter-spacing: 0.5px; margin-top: 4px; }

  .contact { position: absolute; left: 60px; width: 450px; top: 312px; text-align: center; list-style: none; }
  .contact__item { display: flex; flex-direction: column; align-items: center; font-family: var(--sans); font-weight: 300; font-size: 18px; letter-spacing: 0.6px; line-height: 1; margin-bottom: 12px; }
  .contact__icon { display: block; margin-bottom: 3px; }

  .brand-mini { position: absolute; left: 700px; width: 310px; top: 212px; text-align: center; }
  .brand-mini__dot { width: 40px; height: 40px; border-radius: 50%; background: var(--white); margin: 0 auto 40px; }
  .brand-mini__name { font-family: var(--serif); font-weight: 400; font-size: 52px; line-height: 1; letter-spacing: 1px; }
  .brand-mini__since { font-family: var(--serif); font-size: 11px; margin-top: 8px; letter-spacing: 0.3px; }

  .card-back { position: absolute; left: 0; top: 600px; width: 1050px; height: 600px; text-align: center; }
  .brand-main__name { position: absolute; left: 0; right: 0; top: 222px; font-family: var(--serif); font-weight: 400; font-size: 108px; line-height: 1; letter-spacing: 2px; }
  .brand-main__since { position: absolute; left: 0; right: 0; top: 360px; font-family: var(--serif); font-size: 22px; letter-spacing: 0.5px; }
</style>
</head>
<body>
<main class="canvas">
  <section class="card-front">
    <svg class="card-front__shapes" width="1050" height="600" viewBox="0 0 1050 600">
      <rect width="1050" height="600" fill="var(--sky)"/>
      <path class="page-curl" fill="var(--white)" d="M0,0 H410 C470,25 520,110 560,220 C600,330 650,445 700,520 C740,575 785,594 812,600 H0 Z"/>
      <path class="front-panel" fill="var(--navy)" d="M0,0 H410 C470,60 540,200 590,330 C630,440 655,520 668,578 C710,580 750,590 778,600 H0 Z"/>
    </svg>

    <div class="identity">
      <p class="identity__name">Mads Erik Lindvold</p>
      <p class="identity__role">CEO &amp; FOUNDER</p>
    </div>

    <ul class="contact">
      <li class="contact__item">
        <svg class="contact__icon" width="16" height="28" viewBox="0 0 16 28"><rect x="1" y="1" width="14" height="26" rx="2" fill="none" stroke="var(--white)" stroke-width="1.6"/><circle cx="8" cy="23.5" r="1.2" fill="var(--white)"/></svg>
        004791846273
      </li>
      <li class="contact__item">
        <svg class="contact__icon" width="22" height="15" viewBox="0 0 22 15"><rect x="0.5" y="0.5" width="21" height="14" fill="var(--white)"/><path d="M1,1 L11,9 L21,1 M1,14 L8,7 M21,14 L14,7" fill="none" stroke="var(--navy)" stroke-width="1"/></svg>
        korbalt.llc@postmail.com
      </li>
      <li class="contact__item">
        <svg class="contact__icon" width="22" height="22" viewBox="0 0 22 22" fill="none" stroke="var(--white)" stroke-width="1.2"><circle cx="11" cy="11" r="10"/><ellipse cx="11" cy="11" rx="4.5" ry="10"/><path d="M1,11 H21 M3,5.5 H19 M3,16.5 H19 M11,1 V21"/></svg>
        www.korbalt.llc
      </li>
    </ul>

    <div class="brand-mini">
      <div class="brand-mini__dot"></div>
      <p class="brand-mini__name">KORBALT</p>
      <p class="brand-mini__since">SINCE 2026</p>
    </div>
  </section>

  <section class="card-back">
    <p class="brand-main__name">KORBALT</p>
    <p class="brand-main__since">SINCE 2026</p>
  </section>
</main>
</body>
</html>
```